Birch Hollow Lodge & Harbour. A site that will sell our lifestyle and embody our vision.

We are after a fun interactive website for our property development.
Check out our ideas for layout and content.
Use stock videos and phots if we havent provide enough.
Ive attached our Logo.
We are easy to reach and work with. Love the crative process.1.Our Vision.. (This clicks through to vision page)
Nestled in the North East corner of Tesko Lake , Sk amidst thousands of acres of natural beauty, a unique community is taking shape. A community that connectS people, nature and play. A place to find those simpler times.

2.Explore..(This clicks through to explore page)
Discover a new life of adventure, on the lake fishing, in the bush on our trail system or maybe the local golf course.

3. Live Here..(This through to Live page)
Birch Hollow has everything you need to start living a full life based in a thriving community.
Slow down and get to know nature and your neighbors

Target Market(s)

35-65 Lake Life

Coding

Coded - Design and coding required

Number of Pages Required

5+ page

Font styles to use
Other font styles liked:
• Anntonio

Colors
00AB8E
00BBA5
67D7C9
C6EFE9
E9F9F6
F0912C
F2A743
F7CA91
FBE8D2
FDF5EE

Requirements
Nice to have
• Interactive

```html
<!DOCTYPE html>
<html lang="en">
<head>
<meta charset="utf-8">
<title>Birch Hollow Lodge &amp; Harbour</title>
<link rel="stylesheet" href="https://fonts.googleapis.com/css2?family=Oswald:wght@500;600&family=Roboto:wght@400;500;700&display=swap">
<style>
:root{
  --green:#55b04a;
  --green-deep:#3f9a35;
  --green-band:#5cb450;
  --mint:#e7f1e4;
  --ink:#111111;
  --panel:#f5f5f5;
  --muted:#555555;
  --white:#ffffff;
}
*{margin:0;padding:0;box-sizing:border-box}
html,body{width:1200px;height:3453px;overflow:hidden;background:var(--white)}
body{position:relative;font-family:'Roboto',sans-serif;color:var(--ink)}
.abs{position:absolute}
.heading{font-family:'Oswald',sans-serif;font-weight:600;text-transform:uppercase;letter-spacing:.5px}
.heading .accent{color:var(--green)}
.rule{position:absolute;height:5px;width:98px}
.rule::before{content:"";position:absolute;left:0;top:0;width:46px;height:4px;background:var(--ink);transform:skewX(-30deg)}
.rule::after{content:"";position:absolute;left:50px;top:0;width:48px;height:4px;background:var(--green);transform:skewX(-30deg)}
.btn{position:absolute;display:flex;align-items:center;justify-content:center;gap:10px;height:50px;border-radius:30px;background:var(--green);color:var(--white);font-weight:700;font-size:15px;text-transform:uppercase;box-shadow:0 0 0 3px var(--white),0 0 0 5px var(--green);text-decoration:none}
.btn.light{background:var(--white);color:var(--green);box-shadow:0 0 0 3px var(--green),0 0 0 5px var(--white)}
.btn svg{width:15px;height:15px}

/* header */
.site-header{position:absolute;left:0;top:0;width:1200px;height:87px;background:var(--white);z-index:3}
.nav-link{position:absolute;top:36px;font-size:14px;color:#666;text-transform:uppercase}
.nav-link.active{color:var(--ink);font-weight:500}
.nav-link.active::after{content:"";position:absolute;left:0;right:0;bottom:-9px;height:2px;background:var(--green)}
.nav-sep{position:absolute;top:36px;font-size:13px;color:#666}
.brand-badge{position:absolute;left:492px;top:-27px;width:188px;height:180px;border-radius:50%;background:var(--white);z-index:4;display:flex;flex-direction:column;align-items:center;justify-content:flex-end;padding-bottom:40px}
.brand-badge .mark{width:12px;height:12px;border-radius:50%;background:var(--ink);margin-bottom:8px}
.brand-badge .name{font-size:15px;font-weight:700;text-transform:uppercase;line-height:1.2;text-align:center;color:var(--ink)}

/* hero */
.hero{position:absolute;left:0;top:87px;width:1200px;height:743px;overflow:hidden}
.hero-photo{position:absolute;inset:0;background:linear-gradient(180deg,#8b9196 0%,#c7cbce 25%,#aab0b4 45%,#8f8a5a 58%,#556b36 68%,#4f7a34 80%,#3d4a3d 100%)}
.hero-title{position:absolute;left:0;width:1200px;top:131px;text-align:center;font-size:58px;color:var(--white);text-shadow:0 2px 6px rgba(0,0,0,.35)}
.hero-text{position:absolute;left:260px;width:680px;top:215px;text-align:center;color:var(--white);font-size:20px;line-height:32px;text-shadow:0 1px 4px rgba(0,0,0,.4)}
.slide-arrow{position:absolute;top:227px;width:40px;height:40px;border-radius:50%;background:var(--white);display:flex;align-items:center;justify-content:center}
.hero-cut{position:absolute;left:0;top:0}
.scroll-down{position:absolute;left:562px;top:742px;width:76px;height:76px;border-radius:50%;background:var(--white);box-shadow:0 4px 10px rgba(0,0,0,.25);display:flex;align-items:center;justify-content:center;z-index:2}

/* vision */
.vision-bar{position:absolute;left:135px;top:980px;width:60px;height:286px;background:var(--green);border-radius:16px 0 0 16px}
.vision-photo{position:absolute;left:162px;top:908px;width:356px;height:429px;border-radius:16px;background:linear-gradient(160deg,#4a5a3e 0%,#9aa5a8 40%,#c9cdcc 60%,#7d6f5e 85%,#5e5448 100%)}
.vision-panel{position:absolute;left:518px;top:1024px;width:548px;height:278px;background:var(--panel);border-radius:0 18px 18px 0}
.vision-title{position:absolute;left:557px;top:940px;font-size:38px}
.vision-text{position:absolute;left:557px;top:1066px;width:470px;font-size:15px;line-height:27.5px;color:#333;text-align:justify}

/* explore */
.explore{position:absolute;left:0;top:1428px;width:1200px;height:492px;background:var(--mint)}
.section-title{position:absolute;left:0;width:1200px;text-align:center;font-size:38px}
.explore-item{position:absolute;top:189px;width:300px;text-align:center}
.explore-ring{width:156px;height:156px;margin:0 auto;border-radius:50%;background:var(--white);box-shadow:0 6px 16px rgba(0,0,0,.08);display:flex;align-items:center;justify-content:center}
.explore-icon{width:120px;height:120px;border-radius:50%;background:var(--green);display:flex;align-items:center;justify-content:center}
.explore-label{margin-top:34px;font-size:20px;font-weight:500;color:#222}

/* live here */
.live{position:absolute;left:0;top:1920px;width:1200px;height:554px;background:linear-gradient(180deg,#4fa843 0%,var(--green-band) 30%,#5ab34f 100%)}
.live-title{position:absolute;left:109px;top:190px;font-size:38px;color:var(--white)}
.live .rule::before{background:var(--white)}
.live .rule::after{background:var(--white)}
.live-text{position:absolute;left:109px;top:270px;width:424px;font-size:15px;line-height:27.5px;color:var(--white);text-align:justify}
.live-photo-main{position:absolute;left:732px;top:85px;width:356px;height:411px;border:2px solid var(--white);background:linear-gradient(180deg,#a9adbc 0%,#b9bac6 50%,#8b5a4e 70%,#6e3d33 100%)}
.live-photo-small{position:absolute;left:578px;top:226px;width:212px;height:250px;background:linear-gradient(180deg,#2d3428 0%,#c98a72 40%,#b89590 55%,#26301f 80%)}

/* contact */
.field{position:absolute;border-radius:26px;background:var(--white);box-shadow:0 3px 10px rgba(0,0,0,.08);border:1px solid #eee;font-size:13px;color:#888;padding:0 28px;display:flex;align-items:center}
.field.message{align-items:flex-start;padding-top:20px;border-radius:22px}

/* footer */
.site-footer{position:absolute;left:0;top:3024px;width:1200px;height:429px;background:#0a0a0a;color:var(--white)}
.info-item{position:absolute;top:70px;width:240px;text-align:center}
.info-icon{width:84px;height:84px;margin:0 auto;border-radius:50%;border:2px dashed #7cbf3a;display:flex;align-items:center;justify-content:center}
.info-icon span{width:66px;height:66px;border-radius:50%;background:var(--green);display:flex;align-items:center;justify-content:center}
.info-label{margin-top:22px;font-size:13px;font-weight:700;text-transform:uppercase}
.info-value{margin-top:6px;font-size:14px}
.footer-nav{position:absolute;left:0;width:1200px;top:284px;display:flex;justify-content:center;gap:36px;font-size:15px;font-weight:700;text-transform:uppercase}
.footer-line{position:absolute;left:109px;width:976px;top:326px;height:1px;background:#2a2a2a}
.social{position:absolute;top:349px;width:36px;height:36px;border-radius:50%;border:1.5px solid var(--green);display:flex;align-items:center;justify-content:center}
.copyright{position:absolute;right:115px;top:358px;font-size:14px}
</style>
</head>
<body>

<header class="site-header">
  <a class="nav-link active" style="left:182px">Home</a>
  <span class="nav-sep" style="left:244px">|</span>
  <a class="nav-link" style="left:270px">About Us</a>
  <span class="nav-sep" style="left:360px">|</span>
  <a class="nav-link" style="left:385px">Vision</a>
  <a class="nav-link" style="left:718px;top:40px">Explore</a>
  <span class="nav-sep" style="left:801px;top:40px">|</span>
  <a class="nav-link" style="left:826px;top:40px">Live Here</a>
  <a class="btn" style="left:938px;top:24px;width:136px;height:44px;font-size:14px">Contact
    <svg viewBox="0 0 16 16"><circle cx="8" cy="8" r="8" fill="#fff"/><path d="M5 8h6M8.5 5.5 11 8l-2.5 2.5" stroke="#55b04a" stroke-width="1.8" fill="none"/></svg></a>
</header>
<div class="brand-badge">
  <span class="mark"></span>
  <span class="name">Birch Hollow</span>
</div>

<section class="hero">
  <div class="hero-photo" role="img" aria-label="Lakeside homes on a green hillside under a cloudy autumn sky, reflected in calm water"></div>
  <h1 class="heading hero-title">Birch Hollow Lodge &amp; Harbour</h1>
  <p class="hero-text">It was in 1973, while Walt was working for a paving company on a section of HWY 41 North of Cedar Bend, that he discovered Birch Hollow.</p>
  <a class="btn" style="left:514px;top:303px;width:172px">Get Started
    <svg viewBox="0 0 16 16"><circle cx="8" cy="8" r="8" fill="#fff"/><path d="M5 8h6M8.5 5.5 11 8l-2.5 2.5" stroke="#55b04a" stroke-width="1.8" fill="none"/></svg></a>
  <div class="slide-arrow" style="left:84px"><svg width="16" height="16" viewBox="0 0 16 16"><path d="M10 3 5 8l5 5" stroke="#111" stroke-width="2" fill="none"/></svg></div>
  <div class="slide-arrow" style="left:1077px"><svg width="16" height="16" viewBox="0 0 16 16"><path d="M6 3l5 5-5 5" stroke="#111" stroke-width="2" fill="none"/></svg></div>
  <svg class="hero-cut" width="1200" height="743" viewBox="0 0 1200 743">
    <polygon points="0,490 600,700 1200,480 1200,743 0,743" fill="#fff"/>
    <polygon points="0,490 600,700 600,722 0,520" fill="#55b04a"/>
    <polygon points="1167,500 600,700 600,722 1200,515 1200,480" fill="#0a0a0a"/>
  </svg>
</section>
<div class="scroll-down">
  <svg width="32" height="32" viewBox="0 0 32 32"><path d="M8 8l8 8 8-8M8 16l8 8 8-8" stroke="#888" stroke-width="3" fill="none"/></svg>
</div>

<section class="vision">
  <div class="vision-bar"></div>
  <div class="vision-panel"></div>
  <div class="vision-photo" role="img" aria-label="Eagle perched on lakeshore rocks beneath pine branches"></div>
  <h2 class="heading vision-title"><span class="accent">Our</span> Vision</h2>
  <div class="rule" style="left:560px;top:994px"></div>
  <p class="vision-text">Nestled in the North East corner of Tesko Lake,Sk amidst thousands of acres of natural beauty, a unique community is taking shape. A community that connectS people, nature and play. A place to find those simpler times</p>
  <a class="btn" style="left:552px;top:1196px;width:170px">Learn More
    <svg viewBox="0 0 16 16"><circle cx="8" cy="8" r="8" fill="#fff"/><path d="M5 8h6M8.5 5.5 11 8l-2.5 2.5" stroke="#55b04a" stroke-width="1.8" fill="none"/></svg></a>
</section>

<section class="explore">
  <h2 class="heading section-title" style="top:86px"><span class="accent">Our</span> Explore</h2>
  <div class="rule" style="left:552px;top:137px"></div>
  <div class="explore-item" style="left:161px">
    <div class="explore-ring"><div class="explore-icon">
      <svg width="70" height="70" viewBox="0 0 70 70" fill="none" stroke="#fff" stroke-width="2.2"><rect x="10" y="26" width="50" height="34" rx="3"/><path d="M10 44c10-8 18 4 28-4s14-2 22-6"/><path d="M52 10v20M52 10l8 4-8 4"/><circle cx="30" cy="18" r="3"/></svg>
    </div></div>
    <div class="explore-label">The Local Golf&nbsp; Course</div>
  </div>
  <div class="explore-item" style="left:444px">
    <div class="explore-ring"><div class="explore-icon">
      <svg width="70" height="70" viewBox="0 0 70 70" fill="none" stroke="#fff" stroke-width="2.2"><path d="M22 58V36M48 52V34"/><ellipse cx="22" cy="26" rx="9" ry="13"/><ellipse cx="48" cy="24" rx="8" ry="12"/><path d="M30 60c14-4-6-12 10-16s6-10 14-12"/><circle cx="35" cy="14" r="4"/></svg>
    </div></div>
    <div class="explore-label">Our Trail System</div>
  </div>
  <div class="explore-item" style="left:727px">
    <div class="explore-ring"><div class="explore-icon">
      <svg width="70" height="70" viewBox="0 0 70 70" fill="none" stroke="#fff" stroke-width="2.2"><path d="M18 50 56 12"/><path d="M56 12v30"/><path d="M50 42c6-4 10 2 6 8s-8 4-6-8z"/><circle cx="20" cy="38" r="5"/><path d="M14 58l6-12 10 6"/></svg>
    </div></div>
    <div class="explore-label">Lake Fishing in The Bush</div>
  </div>
</section>

<section class="live">
  <h2 class="heading live-title">Live Here</h2>
  <div class="rule" style="left:109px;top:248px"></div>
  <p class="live-text">Birch Hollow has everything you need to start living a full life based in a thriving community.Slow down and get to know nature and your neighbors</p>
  <a class="btn light" style="left:111px;top:386px;width:172px">Learn More
    <svg viewBox="0 0 16 16"><circle cx="8" cy="8" r="8" fill="#55b04a"/><path d="M5 8h6M8.5 5.5 11 8l-2.5 2.5" stroke="#fff" stroke-width="1.8" fill="none"/></svg></a>
  <div class="live-photo-main" role="img" aria-label="Person standing at the end of a red wooden dock on a foggy lake"></div>
  <div class="live-photo-small" role="img" aria-label="Sunset over the lake framed by dark trees"></div>
</section>

<section class="contact">
  <h2 class="heading section-title" style="top:2553px"><span class="accent">Contact</span> Us</h2>
  <div class="rule" style="left:552px;top:2604px"></div>
  <div class="field" style="left:189px;top:2656px;width:393px;height:52px">Name</div>
  <div class="field" style="left:193px;top:2723px;width:393px;height:51px">Email Address</div>
  <div class="field" style="left:193px;top:2789px;width:393px;height:51px">Phone Number</div>
  <div class="field message" style="left:616px;top:2656px;width:395px;height:184px">Message</div>
  <a class="btn" style="left:516px;top:2889px;width:170px">Submit Now
    <svg viewBox="0 0 16 16"><circle cx="8" cy="8" r="8" fill="#fff"/><path d="M5 8h6M8.5 5.5 11 8l-2.5 2.5" stroke="#55b04a" stroke-width="1.8" fill="none"/></svg></a>
</section>

<footer class="site-footer">
  <div class="info-item" style="left:101px">
    <div class="info-icon"><span><svg width="24" height="24" viewBox="0 0 24 24"><path d="M12 2a7 7 0 0 0-7 7c0 5 7 13 7 13s7-8 7-13a7 7 0 0 0-7-7z" fill="#fff"/><circle cx="12" cy="9" r="2.6" fill="#55b04a"/></svg></span></div>
    <div class="info-value" style="margin-top:22px">Birch Hollow Saskatchewan<br>S0X 2B4 Canada</div>
  </div>
  <div class="info-item" style="left:345px">
    <div class="info-icon"><span><svg width="28" height="24" viewBox="0 0 28 24" fill="none" stroke="#fff" stroke-width="2"><rect x="2" y="3" width="24" height="18" rx="2"/><path d="M2 5l12 9 12-9"/></svg></span></div>
    <div class="info-label">Email Address</div>
    <div class="info-value">hello@birchhollowharbour.ca</div>
  </div>
  <div class="info-item" style="left:589px">
    <div class="info-icon"><span><svg width="24" height="24" viewBox="0 0 24 24"><path d="M6 2l4 5-2 3c1 3 3 5 6 6l3-2 5 4-3 4C10 22 2 14 2 5z" fill="#fff"/></svg></span></div>
    <div class="info-label">Phone No</div>
    <div class="info-value">306-555-0148</div>
  </div>
  <div class="info-item" style="left:833px">
    <div class="info-icon"><span><svg width="24" height="26" viewBox="0 0 24 26"><rect x="3" y="8" width="18" height="16" rx="2" fill="#fff"/><rect x="7" y="2" width="10" height="8" fill="none" stroke="#fff" stroke-width="2"/><rect x="7" y="12" width="10" height="3" fill="#55b04a"/><rect x="7" y="17" width="3" height="3" fill="#55b04a"/><rect x="12" y="17" width="3" height="3" fill="#55b04a"/></svg></span></div>
    <div class="info-label">Fax</div>
    <div class="info-value">+ 1 999 999 9999</div>
  </div>
  <nav class="footer-nav">
    <span>Home</span><span>|</span><span>About Us</span><span>|</span><span>Vision</span><span>|</span><span>Explore</span><span>|</span><span>Live Here</span><span>|</span><span>Contact Us</span>
  </nav>
  <div class="footer-line"></div>
  <div class="social" style="left:109px"><svg width="14" height="14" viewBox="0 0 14 14"><circle cx="7" cy="7" r="3" fill="#55b04a"/></svg></div>
  <div class="social" style="left:151px"><svg width="14" height="14" viewBox="0 0 14 14"><circle cx="7" cy="7" r="3" fill="#55b04a"/></svg></div>
  <div class="social" style="left:193px"><svg width="14" height="14" viewBox="0 0 14 14"><circle cx="7" cy="7" r="3" fill="#55b04a"/></svg></div>
  <div class="copyright">©&nbsp; 2023 Copyright&nbsp; Birch Hollow Harbour All Right Reserved.</div>
</footer>

</body>
</html>
```